Videos, Reels, Stories, Shorts, pictures, social media Company

Our company is called, zen reach. We will come to businesses, do content shoot, then through power of ai tools and human interaction, will create great content for clients Snapfolio, Circlebook, and Loopclip account. We will then have content calendar, reporting, and do all of these posts from the content we took and curated pictures and videos to make the reels, stories, shorts, pictures on such platforms. USe what you can for pictures now that you think will look the best. I will fill some in with some of my pictures once I get them made as well.
Updates

For a project this large, I should have provided more time for people to design things. I would like to have a deadline extension so that I can have time to get more designs and review them.

Target Market(s)

small businesses - restaurants, dentists, pet stores, chiropractors, realtors, etc

Industry/Entity Type

social media

Coding

Coded - Design and coding required

Number of Pages Required

5+ page

Colors

Designer to choose colors to be used in the design.

Requirements
Must have
• 5 pages, modern design, gets people to contact us
Nice to have
• nicely designed site, that is not too serious looking, and will pay extra via tipping for someone to make a logo for our company, zen reach

```html
<!DOCTYPE html>
<html lang="en">
<head>
<meta charset="utf-8">
<title>zen reach – Ai tools and human interaction</title>
<link rel="stylesheet" href="https://fonts.googleapis.com/css2?family=Montserrat:wght@400;500;700;800&family=Inter:wght@400;500&display=swap">
<style>
:root{
  --ink:#111118;
  --text:#2a2a33;
  --purple:#5a1fd6;
  --violet:#7b3fe4;
  --cyan:#3fd3ee;
  --lav:#e4e2fb;
  --lav-soft:#f3f1fd;
  --card:#f8f7fe;
  --line:#dcdaf0;
  --white:#ffffff;
}
*{box-sizing:border-box;margin:0;padding:0}
html,body{width:1200px;height:3518px;overflow:hidden}
body{font-family:"Inter",Arial,sans-serif;color:var(--text);background:var(--lav-soft)}
.page{position:relative;width:1200px;height:3518px;overflow:hidden;background:var(--lav-soft)}

/* header */
.site-header{position:absolute;left:0;top:0;width:1200px;height:86px}
.brand{position:absolute;left:97px;top:24px;display:flex;align-items:center;gap:12px}
.brand-dot{width:40px;height:40px;border-radius:50%;background:var(--violet)}
.brand-name{font-family:"Montserrat",sans-serif;font-weight:500;font-size:25px;color:var(--ink)}
.contact-info{position:absolute;left:800px;top:28px;display:flex;align-items:center;gap:12px;font-size:11.5px;line-height:15px;color:var(--ink)}
.btn-contact{position:absolute;left:976px;top:23px;width:126px;height:37px;border-radius:20px;background:linear-gradient(90deg,#3c1fc9,#6a2fe0);color:var(--white);font-size:11px;display:flex;align-items:center;justify-content:center;letter-spacing:.2px}

.main-nav{position:absolute;left:0;top:86px;width:1200px;height:56px;border-top:1px solid var(--line);border-bottom:1px solid var(--line)}
.main-nav .sep{position:absolute;top:0;width:1px;height:56px;background:var(--line)}
.main-nav a{position:absolute;top:20px;font-size:11.5px;color:var(--ink);text-decoration:none}
.nav-icon{position:absolute;top:17px}

/* hero */
.hero-bg{position:absolute;left:0;top:142px;width:1200px;height:560px;background:
 radial-gradient(ellipse 420px 260px at 560px 200px,rgba(63,211,238,.35),transparent 70%),
 radial-gradient(ellipse 500px 300px at 200px 200px,rgba(140,150,255,.25),transparent 70%),
 linear-gradient(180deg,#f4f3fd,#e6e5fb)}
.hero-visual{position:absolute;left:700px;top:170px;width:420px;height:410px;border-radius:50%;background:radial-gradient(circle at 45% 45%,#c9dcf2,#a8b8e6 55%,rgba(200,200,245,0) 75%)}
.hero-kicker{position:absolute;left:102px;top:264px;font-family:"Montserrat",sans-serif;font-size:24px;color:var(--ink)}
.hero-title{position:absolute;left:102px;top:292px;font-family:"Montserrat",sans-serif;font-weight:800;font-size:58px;line-height:68px;color:var(--ink)}

/* services */
.services-band{position:absolute;left:0;top:640px;width:1200px;height:425px;background:linear-gradient(180deg,#ebeafc,#dcdaf8)}
.section-title{font-family:"Montserrat",sans-serif;font-weight:800;color:var(--ink)}
.services-title{position:absolute;left:117px;top:650px;font-size:30px}
.service-card{position:absolute;width:212px;height:187px;background:var(--card);box-shadow:0 4px 14px rgba(90,70,180,.06);text-align:center}
.service-card svg{position:absolute;left:68px;top:18px}
.service-card p{position:absolute;left:18px;right:18px;top:110px;font-size:13px;line-height:17.5px;color:var(--ink)}

/* different */
.different-visual{position:absolute;left:109px;top:1147px;width:348px;height:395px;border-radius:40% 40% 10px 10px;background:radial-gradient(ellipse at 50% 30%,#c98a4a,#e9a13a 45%,rgba(240,170,80,0) 75%)}
.different{position:absolute;left:516px;top:1210px;width:570px}
.different h2{font-size:30px;margin-bottom:34px}
.different p{font-size:12.6px;line-height:17.6px;color:var(--ink);margin-bottom:17px}

/* about */
.about-band{position:absolute;left:0;top:1567px;width:1200px;height:481px;background:linear-gradient(90deg,#e6e4fb,#dedcf8)}
.about-visual{position:absolute;left:587px;top:1567px;width:613px;height:481px;background:radial-gradient(ellipse at 40% 40%,#a43ef0,#7a8ac8 40%,rgba(200,200,240,0) 72%)}
.about-copy{position:absolute;left:123px;top:1650px;width:440px}
.about-copy h2,.why-copy h2{font-size:30px;margin-bottom:30px}
.about-copy p,.why-copy p{font-size:12.6px;line-height:17.6px;color:var(--ink)}

/* why */
.why-band{position:absolute;left:0;top:2048px;width:1200px;height:446px;background:#f7f6fe}
.why-visual{position:absolute;left:48px;top:2062px;width:662px;height:430px;background:radial-gradient(ellipse at 50% 55%,#6fdcec,#d84a6a 30%,rgba(240,240,250,0) 70%)}
.why-copy{position:absolute;left:674px;top:2140px;width:440px}

/* process */
.process{position:absolute;left:0;top:2494px;width:1200px;height:304px;background:#f7f6fe}
.process-title{position:absolute;left:0;width:1200px;top:2530px;text-align:center;font-size:30px}
.step{position:absolute;font-family:"Montserrat",sans-serif;font-weight:500;font-size:19px;color:var(--ink);white-space:nowrap}
.arrow{position:absolute}

/* packages */
.packages-band{position:absolute;left:0;top:2798px;width:1200px;height:635px;background:linear-gradient(180deg,#dedcf9,#e2e0fa)}
.packages-title{position:absolute;left:0;width:1200px;top:2818px;text-align:center;font-size:29px}
.package{position:absolute;top:2883px;width:230px;height:496px;border-radius:48px;background:var(--card);text-align:center;padding:54px 20px 0}
.package h3{font-family:"Montserrat",sans-serif;font-weight:500;font-size:22px;line-height:27px;color:var(--ink);min-height:54px}
.package .price{font-family:"Montserrat",sans-serif;font-weight:800;font-size:36px;margin-top:28px;background:linear-gradient(90deg,var(--purple),var(--cyan));-webkit-background-clip:text;background-clip:text;color:transparent}
.package .term{font-size:14px;line-height:17px;color:var(--ink)}
.package .desc{font-size:13px;line-height:17.4px;color:var(--ink);margin-top:14px}
.package.featured{background:linear-gradient(180deg,#52d7ec 0%,#8a6ee8 38%,#7a2fe4 70%,#6a1fd8 100%)}
.package.featured h3,.package.featured .desc,.package.featured .term{color:rgba(255,255,255,.9)}
.package.featured h3{min-height:81px;color:#e8f6ff}
.package.featured .price{background:none;color:var(--white);margin-top:8px}
.footer-strip{position:absolute;left:0;top:3433px;width:1200px;height:85px;background:var(--lav-soft)}
</style>
</head>
<body>
<div class="page">

  <header class="site-header">
    <div class="brand"><span class="brand-dot"></span><span class="brand-name">zen reach</span></div>
    <div class="contact-info">
      <svg width="22" height="22" viewBox="0 0 24 24"><path d="M6.6 10.8a15 15 0 0 0 6.6 6.6l2.2-2.2a1 1 0 0 1 1-.25 11.4 11.4 0 0 0 3.6.57 1 1 0 0 1 1 1V20a1 1 0 0 1-1 1A17 17 0 0 1 3 4a1 1 0 0 1 1-1h3.5a1 1 0 0 1 1 1c0 1.25.2 2.450.57 3.57a1 1 0 0 1-.25 1z" fill="#3c1fc9"/></svg>
      <div>+01 555 0142<br>info@zenreach.com</div>
    </div>
    <a class="btn-contact">CONTACT US</a>
  </header>

  <nav class="main-nav">
    <span class="sep" style="left:96px"></span><span class="sep" style="left:187px"></span>
    <span class="sep" style="left:294px"></span><span class="sep" style="left:410px"></span>
    <span class="sep" style="left:526px"></span><span class="sep" style="left:668px"></span>
    <span class="sep" style="left:870px"></span><span class="sep" style="left:969px"></span>
    <span class="sep" style="left:1033px"></span><span class="sep" style="left:1102px"></span>
    <a style="left:124px">HOME</a><a style="left:215px">ABOUT US</a><a style="left:329px">SERVICES</a>
    <a style="left:443px">PACKAGES</a><a style="left:558px">CONTACT US</a>
    <svg class="nav-icon" style="left:991px" width="20" height="20" viewBox="0 0 20 20"><path d="M3 5h14M7 9h10M3 13h14M7 17h10" stroke="#111" stroke-width="1.4"/></svg>
    <svg class="nav-icon" style="left:1058px" width="20" height="20" viewBox="0 0 20 20"><circle cx="9" cy="9" r="6" stroke="#111" stroke-width="1.4" fill="none"/><path d="M13.5 13.5 17 17" stroke="#111" stroke-width="1.4"/></svg>
  </nav>

  <section class="hero">
    <div class="hero-bg"></div>
    <div class="hero-visual" role="img" aria-label="Robot head wearing headphones with glowing circuitry"></div>
    <p class="hero-kicker">Use of</p>
    <h1 class="hero-title">Ai tools and<br>human<br>interaction</h1>
  </section>

  <section class="services">
    <div class="services-band"></div>
    <h2 class="section-title services-title">Services:</h2>
    <div class="service-card" style="left:113px;top:696px">
      <svg width="76" height="76" viewBox="0 0 76 76" fill="none" stroke="#6b3fd8" stroke-width="2.2"><rect x="12" y="8" width="44" height="50" rx="2"/><path d="M4 62h68l-4 6H8z"/><path d="M20 18h16M20 26h28M20 34h28M20 42h20"/><path d="M50 48 66 26l4 3-16 22z"/></svg>
      <p>Onsite content making at client’s business using professional equipment.</p>
    </div>
    <div class="service-card" style="left:369px;top:696px">
      <svg width="76" height="76" viewBox="0 0 76 76" fill="none" stroke="#6b3fd8" stroke-width="2.6"><rect x="6" y="18" width="58" height="50" rx="6"/><circle cx="35" cy="43" r="13"/><path d="M31 36v14l11-7z"/><path d="M60 4l3 8 8 3-8 3-3 8-3-8-8-3 8-3z" fill="#3fb8ee" stroke="none"/></svg>
      <p>Editing of videos and pictures using ai tools</p>
    </div>
    <div class="service-card" style="left:624px;top:696px">
      <svg width="76" height="76" viewBox="0 0 76 76" fill="none" stroke="#6b3fd8" stroke-width="2"><rect x="10" y="6" width="56" height="64" rx="2"/><path d="M10 16h56"/><rect x="16" y="22" width="20" height="16"/><path d="M42 24h18M42 30h18M42 36h18M16 46h44M16 52h44M16 58h44M16 64h30"/></svg>
      <p>Creation of newsfeed pictures, videos, also making reels, shorts, stories</p>
    </div>
    <div class="service-card" style="left:875px;top:696px">
      <svg width="76" height="76" viewBox="0 0 76 76" fill="none" stroke="#6b3fd8" stroke-width="2.2"><rect x="6" y="12" width="64" height="58" rx="5"/><path d="M6 26h64M20 6v12M38 6v12M56 6v12"/><g fill="#6b3fd8" stroke="none"><rect x="16" y="34" width="6" height="6"/><rect x="28" y="34" width="6" height="6"/><rect x="40" y="34" width="6" height="6"/><rect x="52" y="34" width="6" height="6"/><rect x="16" y="46" width="6" height="6"/><rect x="28" y="46" width="6" height="6"/><rect x="40" y="46" width="6" height="6"/><rect x="52" y="46" width="6" height="6"/><rect x="16" y="58" width="6" height="6"/><rect x="28" y="58" width="6" height="6"/></g></svg>
      <p>Content calendar</p>
    </div>
    <div class="service-card" style="left:113px;top:932px">
      <svg width="76" height="76" viewBox="0 0 76 76" fill="none" stroke="#6b3fd8" stroke-width="2.2"><rect x="8" y="6" width="62" height="46" rx="2"/><circle cx="24" cy="22" r="7"/><path d="M44 40V30M52 40V22M60 40V16"/><circle cx="26" cy="52" r="11"/><path d="M18 60 6 72"/></svg>
      <p>Competitor analysis</p>
    </div>
    <div class="service-card" style="left:369px;top:932px">
      <svg width="76" height="76" viewBox="0 0 76 76" fill="none" stroke="#6b3fd8" stroke-width="2.2"><rect x="18" y="4" width="40" height="68" rx="5"/><rect x="26" y="16" width="24" height="16" rx="2"/><circle cx="20" cy="48" r="10"/><path d="M34 46h18M34 54h14"/><circle cx="62" cy="22" r="6"/></svg>
      <p>Organic and paid ads<br>(optional)</p>
    </div>
    <div class="service-card" style="left:624px;top:932px">
      <svg width="76" height="76" viewBox="0 0 76 76" fill="none" stroke="#6b3fd8" stroke-width="2"><rect x="8" y="8" width="60" height="58" rx="3"/><path d="M8 18h60"/><rect x="40" y="24" width="22" height="10" rx="2"/><rect x="14" y="40" width="14" height="12"/><path d="M34 42h28M34 48h28M34 54h28M14 60h48"/></svg>
      <p>Content calendar for customer and portal login to view performance</p>
    </div>
    <div class="service-card" style="left:875px;top:932px">
      <svg width="76" height="76" viewBox="0 0 76 76" fill="none" stroke="#6b3fd8" stroke-width="2.2"><rect x="22" y="6" width="32" height="64" rx="5"/><path d="M4 18h22v14H12l-6 5v-5H4z"/><path d="M50 30h22v14h-2v5l-6-5H50z"/><path d="M9 24h12M55 37h12"/></svg>
      <p>Regular reporting<br>to client</p>
    </div>
  </section>

  <section>
    <div class="different-visual" role="img" aria-label="Excited woman in a yellow hoodie holding a laptop and pointing up"></div>
    <div class="different">
      <h2 class="section-title">What makes us different?</h2>
      <p>We harness the power of artificial intelligence (ai) to aid in our services while also providing human customer service. Tired of the same old content? Let’s make things fun by using zen reach! In order to be successful in business, one aspect you need is a well round social media program that includes ongoing content making, editing, posting, using various video and picture ads on Circlebook, Snapfolio, and Loopclip.</p>
      <p>If you are not utilizing reels, stories, shorts, and newsfeed marketing on social media platforms, you simply will not be seen. Get more interactions, followers, leads, and sales with highly creative and tailored video and picture content for your business.</p>
      <p>So, let’s make you and your business a star! Contact us today for a consultation.</p>
    </div>
  </section>

  <section>
    <div class="about-band"></div>
    <div class="about-visual" role="img" aria-label="Robotic hand holding a stack of glowing purple and cyan cubes"></div>
    <div class="about-copy">
      <h2 class="section-title">About Us</h2>
      <p>Lorem ipsum dolor sit amet, consectetur adipisicing elit, sed do eiusmod tempor incididunt ut labore et dolore magna aliqua. Ut enim ad minim veniam, quis nostrud exercitation ullamco laboris nisi ut aliquip ex ea commodo consequat. Duis aute irure dolor in reprehenderit in voluptate velit esse cillum dolore eu fugiat nulla pariatur. Excepteur sint occaecat cupidatat non proident, sunt in culpa qui officia deserunt mollit anim id est laborum.</p>
    </div>
  </section>

  <section>
    <div class="why-band"></div>
    <div class="why-visual" role="img" aria-label="Digital human figure rising from a smartphone surrounded by floating holographic screens"></div>
    <div class="why-copy">
      <h2 class="section-title">Why Choose zen reach?</h2>
      <p>Lorem ipsum dolor sit amet, consectetur adipisicing elit, sed do eiusmod tempor incididunt ut labore et dolore magna aliqua. Ut enim ad minim veniam, quis nostrud exercitation ullamco laboris nisi ut aliquip ex ea commodo consequat. Duis aute irure dolor in reprehenderit in voluptate velit esse cillum dolore eu fugiat nulla pariatur. Excepteur sint occaecat cupidatat non proident, sunt in culpa qui officia deserunt mollit anim id est laborum.</p>
    </div>
  </section>

  <section>
    <div class="process"></div>
    <h2 class="section-title process-title">Our Process</h2>
    <svg width="0" height="0" style="position:absolute"><defs>
      <linearGradient id="arrowGrad" x1="0" x2="1"><stop offset="0" stop-color="#8a6ee8"/><stop offset="1" stop-color="#5ac8f0"/></linearGradient>
      <symbol id="arrowR" viewBox="0 0 56 34"><path d="M2 11h32V3l20 14-20 14v-8H2z" fill="none" stroke="url(#arrowGrad)" stroke-width="2.4" stroke-linejoin="round"/></symbol>
      <symbol id="arrowL" viewBox="0 0 56 34"><path d="M54 11H22V3L2 17l20 14v-8h32z" fill="none" stroke="url(#arrowGrad)" stroke-width="2.4" stroke-linejoin="round"/></symbol>
      <symbol id="arrowCurve" viewBox="0 0 60 44"><path d="M56 2c0 20-14 30-34 30v8L4 28l18-12v8c14 0 26-8 26-22z" fill="none" stroke="url(#arrowGrad)" stroke-width="2.4" stroke-linejoin="round"/></symbol>
      <symbol id="arrowCurveR" viewBox="0 0 60 44"><path d="M4 2c0 20 14 30 34 30v8l18-12-18-12v8C24 24 12 16 12 2z" fill="none" stroke="url(#arrowGrad)" stroke-width="2.4" stroke-linejoin="round"/></symbol>
    </defs></svg>

    <span class="step" style="left:106px;top:2588px">Consultation</span>
    <svg class="arrow" style="left:232px;top:2585px" width="56" height="34"><use href="#arrowR"/></svg>
    <span class="step" style="left:298px;top:2588px">Competitor analysis</span>
    <svg class="arrow" style="left:494px;top:2585px" width="56" height="34"><use href="#arrowR"/></svg>
    <span class="step" style="left:557px;top:2588px">Video and picture content shoot</span>
    <svg class="arrow" style="left:872px;top:2585px" width="56" height="34"><use href="#arrowR"/></svg>
    <span class="step" style="left:941px;top:2588px">Editing</span>

    <span class="step" style="left:225px;top:2637px">Content schedular</span>
    <svg class="arrow" style="left:405px;top:2634px" width="56" height="34"><use href="#arrowL"/></svg>
    <span class="step" style="left:472px;top:2637px">Final product produced</span>
    <svg class="arrow" style="left:708px;top:2634px" width="56" height="34"><use href="#arrowL"/></svg>
    <span class="step" style="left:777px;top:2637px">Production</span>
    <svg class="arrow" style="left:940px;top:2622px" width="60" height="44"><use href="#arrowCurve"/></svg>

    <svg class="arrow" style="left:120px;top:2672px" width="60" height="44"><use href="#arrowCurveR"/></svg>
    <span class="step" style="left:190px;top:2686px">Organic and / or paid posts posts via newsfeed, pictures, videos,&nbsp; reels, shorts, stories, etc.</span>

    <span class="step" style="left:636px;top:2733px;font-size:22px">Success!</span>
    <svg class="arrow" style="left:750px;top:2730px" width="56" height="34"><use href="#arrowL"/></svg>
    <span class="step" style="left:827px;top:2735px">Reporting</span>
    <svg class="arrow" style="left:940px;top:2718px" width="60" height="44"><use href="#arrowCurve"/></svg>
  </section>

  <section>
    <div class="packages-band"></div>
    <h2 class="section-title packages-title">Packages (within 50 miles of Allentown, PA)</h2>

    <article class="package" style="left:100px">
      <h3>Onetime<br>Content Shoot</h3>
      <div class="price">$350.00</div>
      <p class="desc">We come out with our equipment and shoot 3 hours of different types of footage for you. From there, we hand it off the files to you a couple of days later electronically but nothing is made.</p>
    </article>

    <article class="package featured" style="left:358px">
      <h3>Onetime<br>Content Shoot<br>&amp; Curation</h3>
      <div class="price">$699.00</div>
      <p class="term">(one-time fee)</p>
      <p class="desc">Same as number 1, but we also make 3 reels, 3 stories, 3 shorts, 2 newsfeed pictures, and 1 general, 90 second video for your business. From there, we hand it off to you electronically about 1 week later.</p>
    </article>

    <article class="package" style="left:616px">
      <h3>Quarterly</h3>
      <div class="price">$999.00</div>
      <p class="term">per month<br>3 month contract</p>
      <p class="desc">Content Shoot, content curation, creating ongoing content, repurposing existing content, incorporating customer owned content, consistent posting schedule, 5-7 posts on Loopclip per week, daily Snapfolio and Circlebook Stories, 4-6 posts on Snapfolio and Circlebook per week, tracking &amp; reporting provided with customer portal login</p>
    </article>

    <article class="package" style="left:874px">
      <h3>Monthly</h3>
      <div class="price">$1799.00</div>
      <p class="term">per month,<br>3 month contract</p>
      <p class="desc">Monthly / ongoing Quarterly Content Shoot, Curation, creating ongoing content, repurposing existing content, incorporating customer owned content, consistent posting schedule, 5-7 posts on Loopclip per week, daily Snapfolio and Circlebook Stories, 4-6 posts on Snapfolio and Circlebook per week, comment responding, tracking &amp; reporting provided with customer portal login</p>
    </article>
  </section>

  <div class="footer-strip"></div>
</div>
</body>
</html>
```